KDP Mortgage Flyer

We are a mortgage company, advertising for he KDP quickpath program. I would like the following information to be included on the post card:
Most of this information should be on one side of the card
LOWER YOUR KDP MORTGAGE PAYMENT RIGHT NOW

Using the KDP Quickpath program you might be eligible to lower your interest rate and monthly mortgage insurance (MIP) at zero cost to you
The KDP has dramatically reduced its restrictions on Mortgage Insurance Premiums (MIP), combined with rates at historic lows, now is the time to take advantage of the KDP Quickpath Program.

The Quickpath process requires NO APPRAISAL, NO INCOME VERIFICATION, NO ASSET DOCUMENTATION and NO OUT OF POCKET CLOSING COSTS.
What this means to you is:
A REDUCTION IN MONTHLY PAYMENT
POSSIBILITY TO SKIP FIRST TWO MORTGAGE PAYMENTS
SAME TYPE OF 30 YEAR FIXED RATE LOAN – BACKED BY THE KDP
*To qualify for the KDP QUICKPATH you must have a good payment history with zero late payments in the past 12 months

I would like to include our logos on both sides, one side should have the TRC logo as well.
Please have our contact info displayed prominently on both sides
the contact information is as follows and all must be included

Quillan Mortgage
418 Garnet Avenue, Suite 1450
Seattle, WA 98344
Office 206 555 0143
Fax 206 555 0187
Email quickpath@quillanmortgage.com
Tom Wendell - Vice President - MLO-31947
Leo Marsh - Loan Originator

If you could please make the postcard colorful as well as adding some appropriate artwork (home, fence, yard etc) that would be great
thanks so much

```html
<!DOCTYPE html>
<html lang="en">
<head>
<meta charset="utf-8">
<title>Quillan Mortgage – KDP Quickpath Postcard</title>
<link href="https://fonts.googleapis.com/css2?family=Roboto:wght@300;400;700&family=Roboto+Condensed:wght@400;700&display=swap" rel="stylesheet">
<style>
  :root{
    --green:#2f7d32;
    --yellow:#f7c843;
    --grey-text:#707070;
    --grey-band:#d4d4d4;
    --grey-panel-a:#c9c9c9;
    --grey-panel-b:#f2f2f2;
    --brown:#7a2a10;
    --ink:#2b2b2b;
    --red:#e0262b;
    --tick:#4caf2f;
    --page:#e9e9e9;
  }
  *{box-sizing:border-box;margin:0;padding:0}
  html,body{width:1200px;height:800px;overflow:hidden;background:var(--page)}
  .postcard{position:absolute;left:20px;top:20px;width:1160px;height:760px;background:#fff;overflow:hidden;font-family:'Roboto',sans-serif;color:var(--ink)}
  .abs{position:absolute}
  .layer{position:absolute;left:0;top:0}
  .headline{left:44px;top:30px}
  .headline .pre{font-weight:300;font-size:42px;color:var(--grey-text);line-height:1}
  .headline .main{margin-top:10px;font-family:'Roboto Condensed',sans-serif;font-weight:700;font-size:36px;color:var(--green);line-height:1;white-space:nowrap}
  .headline .main span{font-family:'Roboto',sans-serif;font-weight:300;color:var(--grey-text)}
  .yellow-text{left:44px;top:174px;font-size:18px;line-height:26px;color:#3a3a3a;width:620px}
  .yellow-text b{font-family:'Roboto Condensed',sans-serif;font-weight:700;color:#222}
  .green-text{left:44px;top:252px;font-size:18px;line-height:26px;color:#fff;width:690px}
  .green-text b{font-family:'Roboto Condensed',sans-serif;font-weight:700;font-size:21px;letter-spacing:.3px}
  .requires{left:36px;top:382px}
  .requires h3{font-weight:400;font-size:19px;color:#333;margin-bottom:8px}
  .req-list{list-style:none}
  .req-list li{display:flex;align-items:center;gap:12px;font-family:'Roboto Condensed',sans-serif;font-weight:700;font-size:24px;letter-spacing:.5px;color:#1e1e1e;height:37px}
  .benefits{left:470px;top:372px}
  .benefits h3{font-weight:400;font-size:20px;color:#222;margin-bottom:8px}
  .benefit{display:flex;align-items:flex-start;gap:12px;font-family:'Roboto Condensed',sans-serif;font-weight:700;font-size:23px;letter-spacing:.4px;color:var(--brown);line-height:29px;margin-bottom:5px}
  .benefit svg{flex:none;margin-top:4px}
  .benefit.b2{margin-left:24px}
  .benefit.b3{margin-left:48px}
  .footnote{left:700px;top:548px;font-size:14px;line-height:18px;color:#222;width:440px}
  .logo-box{left:40px;top:614px;width:190px;height:132px;background:#fff;display:flex;align-items:center;justify-content:center;gap:8px;box-shadow:0 0 0 1px #ddd}
  .logo-box .dot{width:14px;height:14px;border-radius:50%;background:var(--green)}
  .logo-box .name{font-weight:400;font-size:30px;color:var(--ink)}
  .company{left:262px;top:622px;color:#fff;font-size:17px;line-height:26px;font-style:normal}
  .company strong{font-family:'Roboto Condensed',sans-serif;font-weight:700;font-size:21px}
  .person{font-size:17px;color:#222;white-space:nowrap}
  .person strong{display:block;font-family:'Roboto Condensed',sans-serif;font-weight:700;font-size:23px;color:#1a1a1a;margin-bottom:4px}
  .person small{font-size:14px}
  .person-vp{left:764px;top:640px}
  .person-lo{left:1012px;top:632px}
</style>
</head>
<body>
<main class="postcard">

  <svg class="layer" width="1160" height="760" viewBox="0 0 1160 760" aria-hidden="true">
    <defs>
      <linearGradient id="panelGrey" x1="0" x2="1" y1="0" y2="0">
        <stop offset="0" stop-color="var(--grey-panel-b)"/>
        <stop offset=".55" stop-color="#d9d9d9"/>
        <stop offset="1" stop-color="var(--grey-panel-a)"/>
      </linearGradient>
    </defs>
    <polygon points="30,160 740,160 770,236 30,236" fill="var(--yellow)"/>
    <polygon points="20,242 780,242 840,340 20,340" fill="var(--green)"/>
    <polygon points="0,366 420,366 540,576 0,576" fill="url(#panelGrey)"/>
    <line x1="0" y1="596" x2="1160" y2="596" stroke="#cfcfcf" stroke-width="3"/>
    <rect x="0" y="728" width="1160" height="32" fill="var(--green)"/>
    <polygon points="0,606 690,606 750,760 0,760" fill="var(--green)"/>
    <polygon points="690,614 1160,614 1160,728 744,728" fill="var(--grey-band)"/>
    <line x1="976" y1="622" x2="1010" y2="722" stroke="#222" stroke-width="2"/>
  </svg>

  <svg class="layer" width="1160" height="360" viewBox="0 0 1160 360" role="img" aria-label="Photo: smiling couple sitting on the lawn in front of a yellow house with a tiled roof">
    <defs>
      <linearGradient id="photoTone" x1="0" y1="0" x2="0" y2="1">
        <stop offset="0" stop-color="#b88a5a"/>
        <stop offset=".35" stop-color="#e2b94a"/>
        <stop offset=".7" stop-color="#c9a57e"/>
        <stop offset="1" stop-color="#5f9c2e"/>
      </linearGradient>
    </defs>
    <circle cx="990" cy="40" r="300" fill="url(#photoTone)"/>
    <circle cx="990" cy="40" r="300" fill="none" stroke="var(--green)" stroke-width="12"/>
  </svg>

  <header class="abs headline">
    <div class="pre">Lower Your</div>
    <h1 class="main">KDP MORTGAGE PAYMENT <span>Right Now</span></h1>
  </header>

  <p class="abs yellow-text">Using the KDP Quickpath program you might be eligible to lower your interest rate and monthly <b>Mortgage Insurance (MIP) at zero cost</b> to you.</p>

  <p class="abs green-text">The KDP has dramatically reduced its restrictions on Mortgage Insurance Premiums (MIP), combined with rates at historic lows,<br><b>now is the time to take advantage of the KDP Quickpath Program.</b></p>

  <section class="abs requires">
    <h3>The Quickpath process requires</h3>
    <ul class="req-list">
      <li><svg width="20" height="20" viewBox="0 0 20 20" aria-hidden="true"><circle cx="10" cy="10" r="10" fill="var(--red)"/><path d="M6 6l8 8M14 6l-8 8" stroke="#fff" stroke-width="2.4"/></svg>NO APPRAISAL</li>
      <li><svg width="20" height="20" viewBox="0 0 20 20" aria-hidden="true"><circle cx="10" cy="10" r="10" fill="var(--red)"/><path d="M6 6l8 8M14 6l-8 8" stroke="#fff" stroke-width="2.4"/></svg>NO INCOME VERIFICATION</li>
      <li><svg width="20" height="20" viewBox="0 0 20 20" aria-hidden="true"><circle cx="10" cy="10" r="10" fill="var(--red)"/><path d="M6 6l8 8M14 6l-8 8" stroke="#fff" stroke-width="2.4"/></svg>NO ASSET DOCUMENTATION and</li>
      <li><svg width="20" height="20" viewBox="0 0 20 20" aria-hidden="true"><circle cx="10" cy="10" r="10" fill="var(--red)"/><path d="M6 6l8 8M14 6l-8 8" stroke="#fff" stroke-width="2.4"/></svg>NO OUT OF POCKET CLOSING COSTS.</li>
    </ul>
  </section>

  <section class="abs benefits">
    <h3>What this means to you is:</h3>
    <div class="benefit b1"><svg width="22" height="22" viewBox="0 0 22 22" aria-hidden="true"><circle cx="11" cy="11" r="11" fill="var(--tick)"/><path d="M6 11.5l3.5 3.5L16 8" stroke="#fff" stroke-width="2.6" fill="none"/></svg>A REDUCTION IN MONTHLY PAYMENT</div>
    <div class="benefit b2"><svg width="22" height="22" viewBox="0 0 22 22" aria-hidden="true"><circle cx="11" cy="11" r="11" fill="var(--tick)"/><path d="M6 11.5l3.5 3.5L16 8" stroke="#fff" stroke-width="2.6" fill="none"/></svg>POSSIBILITY TO SKIP FIRST TWO MORTGAGE PAYMENTS</div>
    <div class="benefit b3"><svg width="22" height="22" viewBox="0 0 22 22" aria-hidden="true"><circle cx="11" cy="11" r="11" fill="var(--tick)"/><path d="M6 11.5l3.5 3.5L16 8" stroke="#fff" stroke-width="2.6" fill="none"/></svg><span>SAME TYPE OF 30 YEAR FIXED RATE LOAN<br>&nbsp;- BACKED BY THE KDP</span></div>
  </section>

  <p class="abs footnote">*To qualify for the KDP QUICKPATH you must have a good payment history with zero late payments in the past 12 months</p>

  <div class="abs logo-box"><span class="dot"></span><span class="name">quillan</span></div>

  <address class="abs company">
    <strong>Quillan Mortgage</strong><br>
    418 Garnet Avenue, Suite 1450, Seattle, WA 98344<br>
    Office: 206 555 0143 &nbsp;|&nbsp; Fax: 206 555 0187<br>
    Email: quickpath@quillanmortgage.com
  </address>

  <div class="abs person person-vp"><strong>Tom Wendell</strong>Vice President - <small>MLO-31947</small></div>
  <div class="abs person person-lo"><strong>Leo Marsh</strong>Loan Originator</div>

</main>
</body>
</html>
```